Web Design Project: Facility Management company

Hi! We need a new website.

Our current website: http://www.brantel-group.ru/ and we don-t like it. =)
The structure of our company has changed and now we don't need "cleaning" and "engeneering" on this site.

We are facility management company in Russia. So we provide integrated service solutions specific to industrial services: maintenance, repair, etc. of engineering systems.
More services:
Energy planning
Automation
Audit
Statements with regulators
Video surveillance
Central heating
Security systems
Welding
Management of subcontractors
Electrical installation and service needs
Reception
Catering

Visitors:
* Managers in the field of commercial real estate
* Chief engineers
* TOP managers of large companies, malls, factories...
+ their subordinates
* Small% of applicants.

Here you can see some websites/patterns we liked:
http://www.kvelmort.ru/ (This is our competitor’s site, so our site shouldn’t be an exact copy))))
http://www.orbitask.ru/
http://www.layoutpinery.com/demo/24296.html
http://www.layoutpinery.com/website-templates/10145.html

Style:
Light, hi-tech/minimalizm, the color palette should be based on the original site colors (Green + black + white). http://www.brantel-group.ru/

Estimated sitemap:
1. Home
2. About Us
3. Company's policy
4. History + Achievements.
5. Certificates
6. Map of presence (Here you can use sample map in file "our projects")
7. Services
8. Portfolio
9. News or blog
10. Jobs
11. Contacts - with the feedback form (or the function "call to order")
12. English

Need a design pages: main page, page 404. The rest of the page could be created by general pattern.

Logo, navigation bar and contacts should be visible on all pages of a site.
Flash animation elements and buttons, etc. - not needed.

* We need to develop 3 websites, so we are looking for a long term cooperation.
Looking forward to your creativity =)

Must Have:
Clear, intuitive structure of web pages.
In the center - of pictures reflecting our main services (industrial theme). May be in rotation.
BUT! This banner (central picture) should not be a huge one =)
All relevant information should be visible at once without scrolling.

A possibility to place media files (presentations, video ...) and 2 banner links on the main page.

Font should be available in Cyrillic.
Updates

IMPORTANT!

Please notice that in thisdesign we don't need "cleaning" and "engeneering" on this site.

So don't use old block of 4pictures from our current website. We don't need it anymore. 

Thestructure of our company has changed and now we need some links (may be banners,may be something else) to our future cleaning website as well as engeneeringwebsite.
It should look like seperate (partner) companies, not like our sevices.

Regards, Vera.

Please don't forget that we need bilingual site.

So define language changing tool in your designs.

Industry/Entity Type

Industrial

```html
<!DOCTYPE html>
<html lang="en">
<head>
<meta charset="utf-8">
<title>Brantel Service — Facility Management</title>
<link rel="stylesheet" href="https://fonts.googleapis.com/css2?family=Arimo:ital,wght@0,400;0,700;1,400&family=PT+Sans:wght@400;700&display=swap">
<style>
:root{
  --dark:#1c1d1c;
  --dark-2:#2e302d;
  --green:#809b2c;
  --green-panel:#728d26;
  --green-light:#a8c63c;
  --green-text:#b5d24a;
  --white:#ffffff;
  --black:#000000;
  --grey:#8d8f8c;
}
*{margin:0;padding:0;box-sizing:border-box}
html,body{width:1200px;height:973px;overflow:hidden}
body{position:relative;background:var(--green);font-family:"Arimo",Arial,sans-serif;color:var(--black)}
.abs{position:absolute}
.header-band{left:0;top:0;width:1200px;height:192px;background:radial-gradient(ellipse at 50% 20%,#3b3d3a 0%,var(--dark-2) 40%,var(--dark) 100%);border-top:2px solid var(--green-light)}
.header-bar{left:232px;top:29px;width:746px;height:25px;border-radius:3px;background:linear-gradient(180deg,#6a6c69 0%,#b9bbb8 45%,#707270 100%);opacity:.85}
.brand{left:480px;top:18px;width:240px;height:44px;background:var(--dark);display:flex;align-items:center;justify-content:center;gap:8px;font-family:"PT Sans",sans-serif;font-size:22px;letter-spacing:3px;color:var(--white)}
.brand-dot{width:12px;height:12px;border-radius:50%;background:var(--green-light)}
.lang{left:764px;top:11px;display:flex;align-items:center;gap:6px;color:var(--white);font:700 11px "PT Sans",sans-serif}
.phone-icon{left:384px;top:29px}
.phone{left:356px;top:58px;color:var(--green-text);font:700 9.5px "Arimo",sans-serif;text-shadow:0 0 2px #000}
.also{left:345px;top:110px;width:93px;text-align:center;color:var(--white);font:700 15px "PT Sans",sans-serif}
.also span{color:var(--green-text)}
.partner{left:345px;width:93px;height:14px;background:var(--green-light);color:var(--white);font:700 8.5px "Arimo",sans-serif;text-align:center;line-height:14px}
.thumb-icon{left:377px;top:183px}
.group-name{left:340px;top:211px;width:100px;text-align:center;color:var(--white);font:700 11px/12px "Arimo",sans-serif}
.site-ghost{left:340px;top:255px;width:100px;text-align:center;color:#a9b98a;font:700 9.5px "Arimo",sans-serif}
.card{top:79px;width:138px;height:205px;border:2px solid var(--white);background:var(--white)}
.card-image{position:absolute;left:2px;top:2px;width:130px;height:153px}
.card-image span{position:absolute;left:0;right:0;bottom:8px;text-align:center;color:var(--white);font:700 10px/11px "Arimo",sans-serif;text-shadow:0 0 3px #000}
.card-caption{position:absolute;left:2px;top:159px;width:130px;height:40px;background:var(--green-light);color:var(--white);font:700 9px/11px "Arimo",sans-serif;display:flex;align-items:center;justify-content:center;text-align:center}
.company-title{left:753px;top:75px;color:var(--white);font:700 16px "PT Sans",sans-serif}
.company-title span{color:#cfd0cc;font-size:17px}
.company-rule{left:751px;top:97px;height:175px;border-left:2px dashed var(--white)}
.company-menu{left:760px;top:105px;list-style:none}
.company-menu li{height:14.4px;display:flex;align-items:center;gap:6px;font:700 8.5px "Arimo",sans-serif}
.company-menu li i{width:9px;height:9px;border:1px solid #999;background:#111;display:block}
.company-menu a{color:var(--white)}
.tagline{left:300px;top:296px;width:604px;text-align:center;color:var(--white);font:700 14.5px/16px "Arimo",sans-serif;letter-spacing:.5px;text-shadow:0 1px 2px #333}
.tagline span{color:var(--green-light);text-shadow:0 0 1px #fff}
.tagline-dash{left:510px;top:333px;width:178px;border-top:3px dashed var(--white)}
.service-strip{left:336px;top:346px;width:535px;height:19px;border-radius:4px;background:var(--black);border:1px solid #555;color:var(--white);font:700 8.5px "Arimo",sans-serif;display:flex;align-items:center;justify-content:center}
.section-title{left:336px;top:389px;width:535px;text-align:center;font:700 17.5px "Arimo",sans-serif}
.panel{top:415px;height:443px;background:var(--green-panel)}
.submenu{left:336px;width:104px;padding:17px 0 0 5px}
.submenu h3{font:700 11.5px "Arimo",sans-serif;margin-bottom:7px}
.submenu ul{list-style:none;padding-left:10px}
.submenu li{height:14.4px;font:700 7.5px "Arimo",sans-serif}
.submenu a,.footer-menu a{color:var(--white)}
.content{left:444px;width:291px;padding:15px 7px 0 7px;font-size:6.8px;line-height:8.2px;color:#111}
.content p{margin-bottom:8px}
.content h4{color:var(--white);font:700 8.5px "Arimo",sans-serif;margin:2px 0 9px}
.content ul{list-style:none;padding-left:13px;margin-bottom:9px;font-style:italic}
.extra{left:739px;width:132px;padding:17px 8px 0 8px;font:700 7px/8.2px "Arimo",sans-serif}
.extra ul{list-style:none;margin-top:8px}
.extra li{color:var(--white);line-height:10.8px}
.extra li::before{content:"- ";color:var(--black)}
.footer-title{left:0;top:875px;width:1200px;text-align:center;font:700 11px "Arimo",sans-serif}
.footer-menu{left:0;top:893px;width:1200px;text-align:center;font:700 7.5px "Arimo",sans-serif}
.footer-brand{left:540px;top:920px;width:120px;text-align:center;color:var(--white);font:400 13px "PT Sans",sans-serif;letter-spacing:2px;display:flex;align-items:center;justify-content:center;gap:6px}
.footer-brand i{width:8px;height:8px;border-radius:50%;background:var(--white);display:block}
.copyright{left:0;top:954px;width:1200px;text-align:center;font:8px "Arimo",sans-serif}
</style>
</head>
<body>
<div class="abs header-band"></div>
<div class="abs header-bar"></div>
<div class="abs brand"><i class="brand-dot"></i>BRANTEL SERVICE</div>

<div class="abs lang">
  <svg width="16" height="12" viewBox="0 0 16 12"><rect width="16" height="4" fill="#fff"/><rect y="4" width="16" height="4" fill="#1c3f9f"/><rect y="8" width="16" height="4" fill="#d52b1e"/></svg>
  Русский
</div>

<svg class="abs phone-icon" width="24" height="24" viewBox="0 0 24 24"><circle cx="12" cy="12" r="11" fill="#6d7a3a" stroke="#d8e5a0" stroke-width="1.5"/><path d="M8.5 6.5l2 0 1 3-1.3 1a7 7 0 0 0 3.3 3.3l1-1.3 3 1v2a1.5 1.5 0 0 1-1.5 1.5A9.5 9.5 0 0 1 7 8a1.5 1.5 0 0 1 1.5-1.5z" fill="#fff"/></svg>
<div class="abs phone">+ 7 812 555 0142</div>

<div class="abs also">Also <span>visit</span></div>
<a class="abs partner" style="top:133px">Cleaning website</a>
<a class="abs partner" style="top:149px">Engineering website</a>

<svg class="abs thumb-icon" width="24" height="24" viewBox="0 0 24 24"><circle cx="12" cy="12" r="11" fill="#6e8a26" stroke="#fff" stroke-width="1.5"/><path d="M7 11h3v7H7zM11 11l3-5c1 0 1.5 1 1 2.5l-.5 1.5H18l-1 8h-6z" fill="#fff"/></svg>
<div class="abs group-name">BRT - TM - FM<br>company</div>
<div class="abs site-ghost">brantel-group.ru</div>

<div class="abs card" style="left:462px">
  <div class="card-image" role="img" aria-label="Glass office tower reflecting blue sky and clouds" style="background:linear-gradient(180deg,#2f6fb4 0%,#7fb0de 45%,#d9e8f5 70%,#5c8fc4 100%)"><span>Click here to<br>learn more</span></div>
  <div class="card-caption">Integrated facility<br>management</div>
</div>
<div class="abs card" style="left:606px">
  <div class="card-image" role="img" aria-label="White industrial pipes on a textured wall" style="background:linear-gradient(135deg,#e6e6e4 0%,#bdbdbb 50%,#8e8f8d 100%)"><span>Click here to<br>learn more</span></div>
  <div class="card-caption">Technical maintenance of<br>engineering systems</div>
</div>

<div class="abs company-title">Our <span>Company</span></div>
<div class="abs company-rule"></div>
<ul class="abs company-menu">
  <li><i></i><a href="#">Home</a></li>
  <li><i></i><a href="#">About Us</a></li>
  <li><i></i><a href="#">Company's policy</a></li>
  <li><i></i><a href="#">History + Achievements.</a></li>
  <li><i></i><a href="#">Certificates</a></li>
  <li><i></i><a href="#">Map of presence</a></li>
  <li><i></i><a href="#">Services</a></li>
  <li><i></i><a href="#">Portfolio</a></li>
  <li><i></i><a href="#">News or blog</a></li>
  <li><i></i><a href="#">Jobs</a></li>
  <li><i></i><a href="#">Contacts</a></li>
</ul>

<div class="abs tagline">A team of <span>specialists</span> for all your needs in<br>commercial property <span>management</span> and <span>maintenance</span></div>
<div class="abs tagline-dash"></div>
<div class="abs service-strip">Commercial property management &nbsp;-&nbsp; Complex maintenance of immovable property &nbsp;-&nbsp; Commercial property maintenance service</div>

<h2 class="abs section-title">- Section Title Here -</h2>

<nav class="abs panel submenu">
  <h3>SubMenu</h3>
  <ul>
    <li><a href="#">Home</a></li><li><a href="#">About Us</a></li><li><a href="#">Company's policy</a></li>
    <li><a href="#">History + Achievements.</a></li><li><a href="#">Certificates</a></li><li><a href="#">Map of presence</a></li>
    <li><a href="#">Services</a></li><li><a href="#">Portfolio</a></li><li><a href="#">News or blog</a></li>
    <li><a href="#">Jobs</a></li><li><a href="#">Contacts</a></li>
  </ul>
</nav>

<main class="abs panel content">
  <p>These are the most important aspects of acquisition of the highest possible incomes from the commercial property object's operation regardless of their purpose: it can be production, business center, a building of a shop, bank, restaurant, warehousing logistic complex, hotel or the biggest shopping and recreation center.</p>
  <p>More and more modern companies – proprietors and developer companies, hand over maintenance of the buildings, structures with all installation for outsourcing to a professional management company.</p>
  <h4>Why do they choose us?</h4>
  <p>Following the complex approach to management problems, we will help to optimize maintenance costs and your immovable property service.</p>
  <p>We use an accumulated experience of immovable property maintenance, any kind of engineering systems, and their modernization for extension of durability time, and you save your money.</p>
  <h4>What can we do?</h4>
  <p>Our own team of professionals will organize and provide:</p>
  <ul>
    <li>commercial property management</li><li>maintenance of immovable property</li><li>maintenance of dangerous industrial objects</li>
    <li>maintenance and technical service of plants and factories</li><li>technical service of industrial and production equipment</li>
    <li>technical service of engineering systems and equipment of any complexity</li><li>professional cleaning</li>
    <li>designing and installation of engineering systems</li><li>reconstruction and modernization of engineering systems</li>
    <li>outsourcing &amp; staff leasing</li><li>work with oversight bodies and government services</li>
  </ul>
  <p>Engineering audit and control system of the provided services quality let us estimate and control on a regular basis, correct organization and technical procedures on timely basis at all the stages of performance of the work.</p>
  <p>This system let predict the budget and plan the works needed to be performed on your immovable property objects in the future.</p>
  <p>At your service is a team of highly experienced managers and qualified engineers.</p>
  <p>Comprehensive liability insurance will reduce the risks connected with possible losses in any contingency.</p>
  <p>In accordance with your desire, we can work around-the-clock (24/7), come ringdown or according to the scheduled plan. Flexibility in the variants of our cooperation is the earnest of your success.</p>
</main>

<aside class="abs panel extra">
  <p>We are facility management company in Russia. So we provide integrated service solutions specific to industrial services: maintenance, repair, etc. of engineering systems.</p>
  <p style="margin-top:9px">Plus:</p>
  <ul>
    <li>Energy planning</li><li>Automation</li><li>Audit</li><li>Statements with regulators</li><li>Video surveillance</li>
    <li>Central heating</li><li>Security systems</li><li>Welding</li><li>Management of subcontractors</li>
    <li>Electrical installation and<br>&nbsp;&nbsp;service needs</li><li>Reception</li><li>Catering</li>
  </ul>
</aside>

<div class="abs footer-title">Main Menu</div>
<div class="abs footer-menu"><a href="#">Home . About Us . Company's policy . History + Achievements . Certificates . Map of presence &nbsp;. Services . Portfolio . News or blog . Jobs . Contacts</a></div>
<div class="abs footer-brand"><i></i>BRANTEL</div>
<div class="abs copyright">© Brantel 2012</div>
</body>
</html>
```